Product label for premium fruit wooden crates

Background: KelVaro offers premium quality fruits airflown (i.e. Japan, USA, Australia, etc) to Singapore at an affordable price. This includes exquisite and limited fruits like Shine Muscat grape, Shizuoka Crown Melon, Yellow Dragon Fruit, Fei zi xiao seedless lychee, Yellow Peaches, etc.

Requirements:

- Design a premium fruit’s label strap for identification and brand marketing.

- This strap will be used to tie around our fruit gift crate and fruit boxes (see attached).

- the logo use in this strap may use different color that must fit the 2 ribbons that will be used together with the crate box (see attached), red and gold ribbons(purl satin)

- the fruit crates and boxes will be presented as gift for vip, families, and working partners (important people)

This label will be printed in paper and tie around the fruit crate or paper box.

Web: www.kelvaro.sg
FB: https://www.facebook.com/kvrorch/
IG: https://www.instagram.com/kvrorch

Target Market(s)

Working class, families, expat, business clients (late 20 – 40s)

Industry/Entity Type

Gift Shop

Font styles to use
Other font styles liked:
• Sakkal Majalla

Requirements
Must have
• - color that fit the 2 ribbons color (red and gold)
• - premium, luxury and exquisite feel
• - presentable as a gift to someone important
• - Kelvaro's logo
• - The word 'KELVARO',
Nice to have
• the following words:
• - www.kelvaro.sg; or/and
• - online premium fruits or/and
• - premium quality (No preference. let the designer choose)
• must be able to give customer a feel that Kelvaro sells premium fruits
Should not have
• cant think of it now

```html
<!DOCTYPE html>
<html lang="en">
<head>
<meta charset="utf-8">
<title>KELVARO – Crate Label Strap</title>
<link rel="stylesheet" href="https://fonts.googleapis.com/css2?family=Marcellus&display=swap">
<style>
  :root {
    --paper: #ffffff;
    --strap-red: #d71f30;
    --ribbon-gold: #f7b977;
    --gold-text: #f8c47e;
    --badge-pink: #e5607a;
    --badge-edge: #e6e6e6;
  }
  html, body {
    margin: 0;
    padding: 0;
    overflow: hidden;
    background: var(--paper);
  }
  .label-strap {
    position: relative;
    width: 1200px;
    height: 178px;
    background: var(--paper);
    overflow: hidden;
    font-family: "Marcellus", serif;
  }
  .strap-band {
    position: absolute;
    left: 0;
    top: 46px;
    width: 1200px;
    height: 112px;
    background: var(--strap-red);
  }
  .gold-stripe {
    position: absolute;
    left: 0;
    width: 1200px;
    height: 5px;
    background: var(--ribbon-gold);
  }
  .gold-stripe--top { top: 59px; }
  .gold-stripe--bottom { top: 140px; }
  .strap-text {
    position: absolute;
    top: 100px;
    transform: translateY(-50%);
    color: var(--gold-text);
    white-space: nowrap;
    line-height: 1;
  }
  .web-address { left: 6px; font-size: 19px; }
  .brand-name { font-size: 18px; letter-spacing: 0.5px; }
  .brand-name--left { left: 349px; }
  .brand-name--right { left: 1093px; }
  .tagline { left: 728px; font-size: 22px; }
  .brand-dot {
    position: absolute;
    top: 100px;
    width: 44px;
    height: 44px;
    margin-top: -22px;
    border-radius: 50%;
    background: var(--badge-pink);
  }
  .brand-dot--left { left: 248px; }
  .brand-dot--right { left: 930px; }
  .center-badge {
    position: absolute;
    left: 514px;
    top: 4px;
    width: 172px;
    height: 172px;
    border-radius: 50%;
    background: var(--paper);
    box-shadow: 0 0 0 1px var(--badge-edge);
    display: flex;
    align-items: center;
    justify-content: center;
  }
  .center-badge__name {
    font-size: 22px;
    letter-spacing: 1px;
    color: var(--badge-pink);
  }
</style>
</head>
<body>
  <div class="label-strap">
    <div class="strap-band"></div>
    <div class="gold-stripe gold-stripe--top"></div>
    <div class="gold-stripe gold-stripe--bottom"></div>

    <span class="strap-text web-address">www.kelvaro.sg</span>
    <span class="brand-dot brand-dot--left"></span>
    <span class="strap-text brand-name brand-name--left">KELVARO</span>

    <div class="center-badge">
      <span class="center-badge__name">KELVARO</span>
    </div>

    <span class="strap-text tagline">premium quality</span>
    <span class="brand-dot brand-dot--right"></span>
    <span class="strap-text brand-name brand-name--right">KELVARO</span>
  </div>
</body>
</html>
```